New Business Card for Auto Repair and Performance Shop!

Need a redesign on a card that we have used for a while now. Something more update and modern, Serious but not too serious. Something confident, that shows the client that we are bespoke. Adding value.

Target Market(s)

Foreign Auto Repair and Performance

Industry/Entity Type

Automotive

Contact Information for Business Card

Utilize Logo, would like to change car silhouette to something Veltra,

Font styles to use
Sans Serif

Requirements
Must have
• business name, address, website, phone number.
MotoSerenix
4918 W. Birchwell Rd
Killeen, T.X. 76542
1-254-487-3106
www.moto-serenix-example.com

Specializing in Asian, European, and Domestic Auto Repair, Performance and Fabrication.

Clear space on back to for space to write appointment time and which client advisor helped the client.
Nice to have
• Up to the designers,

```html
<!DOCTYPE html>
<html lang="en">
<head>
<meta charset="utf-8">
<title>MotoSerenix Business Card</title>
<link rel="stylesheet" href="https://fonts.googleapis.com/css2?family=Teko:wght@300;400;500&display=swap">
<style>
  :root {
    --stage: #b9b9b9;
    --card: #0b0b0b;
    --card-edge: #161616;
    --red: #e2393d;
    --silver: #cfcfcf;
    --white: #ffffff;
    --ink: #2b2b2b;
    --rule: #9a9a9a;
  }
  * { margin: 0; padding: 0; box-sizing: border-box; }
  html, body { width: 1050px; height: 1200px; overflow: hidden; }
  body {
    background: var(--stage);
    font-family: "Teko", sans-serif;
    position: relative;
  }
  .card {
    position: absolute;
    background: radial-gradient(ellipse at 50% 40%, var(--card-edge), var(--card) 70%);
    box-shadow: 6px 8px 10px rgba(0,0,0,0.35);
    overflow: hidden;
  }
  .card--front { left: 170px; top: 139px; width: 711px; height: 435px; }
  .card--back  { left: 169px; top: 619px; width: 712px; height: 442px; }

  .brand-name {
    position: absolute;
    color: var(--silver);
    font-weight: 400;
    letter-spacing: 4px;
    line-height: 1;
    white-space: nowrap;
  }
  .card--front .brand-name { left: 0; width: 100%; text-align: center; top: 110px; font-size: 58px; }
  .card--back .brand-name { right: 48px; top: 350px; font-size: 42px; }

  .specialty-band {
    position: absolute;
    left: 0; top: 246px; width: 100%; height: 116px;
    background: linear-gradient(#2c2c2c, #050505 45%, #000);
    border-top: 3px solid #8c8c8c;
    border-bottom: 3px solid #8c8c8c;
  }
  .specialty-pill {
    position: absolute;
    left: 258px; top: 232px; width: 193px; height: 34px;
    border-radius: 17px;
    background: linear-gradient(#2a2a2a, #000);
    border: 2px solid #b8b8b8;
    color: var(--red);
    font-weight: 500;
    font-size: 30px;
    line-height: 36px;
    text-align: center;
    letter-spacing: 0.5px;
  }
  .specialty-text {
    position: absolute;
    left: 0; top: 276px; width: 100%;
    text-align: center;
    color: var(--white);
    font-weight: 300;
    font-size: 34px;
    line-height: 37px;
    letter-spacing: 0.5px;
  }

  .contact-row {
    position: absolute;
    left: 52px; top: 382px; right: 30px;
    display: flex; gap: 26px;
    color: var(--white);
    font-weight: 300;
    font-size: 22px;
  }
  .contact-item { display: flex; align-items: center; gap: 5px; white-space: nowrap; }
  .contact-item svg { width: 19px; height: 19px; flex: none; }

  .contact-list {
    position: absolute;
    left: 44px; top: 310px;
    list-style: none;
    color: var(--white);
    font-weight: 300;
    font-size: 22px;
  }
  .contact-list .contact-item { height: 33px; }

  .appointment-panel {
    position: absolute;
    left: 28px; top: 22px; width: 667px; height: 235px;
    background: var(--white);
    border-radius: 42px 42px 0 0;
  }
  .field-label {
    position: absolute;
    left: 35px;
    color: var(--ink);
    font-weight: 300;
    font-size: 24px;
    line-height: 1;
  }
  .field-rule {
    position: absolute;
    right: 27px;
    height: 1.5px;
    background: var(--rule);
  }
</style>
</head>
<body>

<svg width="0" height="0" style="position:absolute">
  <defs>
    <symbol id="icon-pin" viewBox="0 0 20 20">
      <circle cx="10" cy="10" r="9" fill="none" stroke="#e2393d" stroke-width="1.2"/>
      <path d="M10 4.5a3.6 3.6 0 0 0-3.6 3.6c0 2.7 3.6 6.9 3.6 6.9s3.6-4.2 3.6-6.9A3.6 3.6 0 0 0 10 4.5z" fill="#e2393d"/>
      <circle cx="10" cy="8.1" r="1.4" fill="#0b0b0b"/>
    </symbol>
    <symbol id="icon-phone" viewBox="0 0 20 20">
      <circle cx="10" cy="10" r="9" fill="none" stroke="#e2393d" stroke-width="1.2"/>
      <path d="M6.3 5.2l2 .1.9 2.4-1.2 1a6.5 6.5 0 0 0 3.3 3.3l1-1.2 2.4.9.1 2c-.2.6-.8.9-1.5.9-4.3-.3-7.6-3.6-7.9-7.9 0-.7.3-1.3.9-1.5z" fill="#e2393d"/>
    </symbol>
    <symbol id="icon-globe" viewBox="0 0 20 20">
      <circle cx="10" cy="10" r="9" fill="none" stroke="#e2393d" stroke-width="1.2"/>
      <circle cx="10" cy="10" r="5.5" fill="none" stroke="#e2393d" stroke-width="1"/>
      <ellipse cx="10" cy="10" rx="2.4" ry="5.5" fill="none" stroke="#e2393d" stroke-width="1"/>
      <path d="M4.5 10h11M5.3 7.3h9.4M5.3 12.7h9.4" stroke="#e2393d" stroke-width="1"/>
    </symbol>
  </defs>
</svg>

<section class="card card--front">
  <div class="brand-name">MotoSerenix</div>

  <div class="specialty-band"></div>
  <div class="specialty-pill">SPECIALIZING IN</div>
  <p class="specialty-text">ASIAN, EUROPEAN, AND DOMESTIC AUTO REPAIR,<br>PERFORMANCE AND FABRICATION.</p>

  <div class="contact-row">
    <span class="contact-item"><svg><use href="#icon-pin"/></svg>4918 W. Birchwell Rd Killeen, T.X. 76542</span>
    <span class="contact-item"><svg><use href="#icon-phone"/></svg>1-254-487-3106</span>
    <span class="contact-item"><svg><use href="#icon-globe"/></svg>www.moto-serenix-example.com</span>
  </div>
</section>

<section class="card card--back">
  <div class="appointment-panel">
    <span class="field-label" style="top:44px">Appointment Time</span>
    <span class="field-rule" style="top:57px; left:163px"></span>
    <span class="field-rule" style="top:102px; left:35px"></span>
    <span class="field-label" style="top:131px">Client Advisor</span>
    <span class="field-rule" style="top:148px; left:135px"></span>
    <span class="field-rule" style="top:198px; left:35px"></span>
  </div>

  <ul class="contact-list">
    <li class="contact-item"><svg><use href="#icon-globe"/></svg>www.moto-serenix-example.com</li>
    <li class="contact-item"><svg><use href="#icon-phone"/></svg>1-254-487-3106</li>
    <li class="contact-item"><svg><use href="#icon-pin"/></svg>4918 W. Birchwell Rd Killeen, T.X. 76542</li>
  </ul>

  <div class="brand-name">MotoSerenix</div>
</section>

</body>
</html>
```